Quiet Horizon Splash page

We want a page to educate the facility managers of Office buildings on the wasted lighting that is left on at night time in their buildings. The page should encourage them to reach out to us for ways to reduce/eliminate the wasted lighting.
Part of the motivation is created by showing photographs of city skylines, and highlight specific buildings, and floors in buildings that have lights left on when the light is not needed. We have attached photos of the San Francisco and LA skylines. We have also created a page with ClipHub videos educating on light pollution. http://www.velotransit-example.com/education-center-2/velotransit-video-library/
Details:
- We would like a graphic on the page that is the symbol to represent the Quiet Horizon we are working to create.
- The page should be able to segment different cities
- The page should be stand alone with enough information to be valuable, but also should link into more details
- The page should tie into our existing site www.velotransit-example.com
- The page should motivate people to eliminate their wasted light by contacting us
Updates

Hi all, We have received a number of designs, and some are close to our expectation. We will choose a 1st and 2nd place tomorrow night. Here is more clarification based on the designs being submitted: (Please edit your submission if it does not match with the notes below) 1. This design is Not for a homepage or to represent VeloTransit corporately. This design is only to do an interior page that will be the Quiet Horizon initiative. 2. The "Symbol to represent the Quiet Horizon" is a graphic, logo or image that can universally be recognized as representing our Quiet Horizon initiative. This would be used on the webpage and literature we may develop in the future. 3. We expect people visiting this Quiet Horizon page to ask a couple questions. * "What is the Quiet Horizon?" * Is my building causing the wasted lighting (Can I look at a photo of my city {San Francisco, Los Angeles, New York City} and see my building lit up at night? * Is VeloTransit creating a Quiet Horizon? (See images from every 6 months of the same city skyline to see how it is changing) 4. The webpage should not focus on the specific capabilities, skills, tools or software of VeloTransit. It should only focus on the Who, What, Where, Why, How of creating a Quiet Horizon.

Here are notes to help with the design: - Use our uploaded skyline images. - Highlight a level of light left on in those images. and note, "Is your lighting wasted for hours every night?" - Highlight a dark area of a building in those images and note "We helped create a Quiet Horizon here!" - Add an email address to contact us at the bottom and say, "I want to be part of the Quiet Horizon in my city!""

Hi All Designers, Sorry for the delay while I was traveling the past week. We had 62 designs submitted and we have narrowed it down to 7. We are voting this week on designs that are best and then we will choose First place and Second place awards. Thanks! Peter

Target Market(s)

Owners and managers of large office buildings in Western speaking countries. Generally adult male aged 30-60.

Industry/Entity Type

Education

Requirements
Must have
• Sectioned areas for different cities based on where the person is visiting our website from. Major cities we focus on include: Los Angeles, San Francisco, New York City, Philadelphia
Nice to have
• Graphic or image logo representing the Quiet Horizon.
Should not have
• Do not focus on VeloTransit. Focus on the Quiet Horizon initiative.

```html
<!DOCTYPE html>
<html lang="en">
<head>
<meta charset="utf-8">
<title>Quiet Horizon</title>
<link href="https://fonts.googleapis.com/css2?family=Open+Sans:wght@400;700;800&family=Ubuntu:wght@300;400;500;700&display=swap" rel="stylesheet">
<style>
:root{
  --green:#8cc63f;
  --cream:#f6f1e6;
  --sand:#ebe5d4;
  --ink:#4a4a48;
  --ink-soft:#6a6a66;
  --night:#141414;
  --night-deep:#232323;
  --white:#ffffff;
}
*{margin:0;padding:0;box-sizing:border-box}
html,body{width:1200px;height:2707px;overflow:hidden;background:var(--cream)}
body{font-family:"Ubuntu",sans-serif;color:var(--ink)}
.page{position:relative;width:1200px;height:2707px;overflow:hidden;background:var(--cream)}
.abs{position:absolute}

.topbar{left:0;top:0;width:1200px;height:50px;background:var(--green)}
.topbar-search{left:970px;top:0;width:230px;height:50px;background:#2b2b2b}
.social{display:flex;gap:13px;left:131px;top:15px}
.social span{width:19px;height:19px;border-radius:50%;background:var(--white)}
.search-icon{left:1050px;top:14px}

.brand{left:131px;top:92px;display:flex;align-items:center;gap:12px}
.brand-square{width:30px;height:30px;border:3px solid var(--green)}
.brand-name{font-size:33px;font-weight:400;color:var(--ink)}

.nav{left:137px;top:175px;display:flex;gap:27px;font-family:"Open Sans",sans-serif;font-weight:700;font-size:14px;text-transform:uppercase;color:var(--ink)}
.nav .active{color:var(--green)}

.hero{left:131px;top:248px;width:936px;height:490px;overflow:hidden}
.hero-photo{position:absolute;top:0;height:490px;width:468px}
.hero-photo.left{left:0;background:linear-gradient(180deg,#1b2a5c 0%,#26306a 40%,#6a4a2a 75%,#2a1d18 100%)}
.hero-photo.right{left:468px;background:linear-gradient(180deg,#0d0d10 0%,#1e1c1a 55%,#3a3020 80%,#0c0c0c 100%)}
.hero-line{position:absolute;top:0;width:468px;text-align:center;font-family:"Open Sans",sans-serif;font-weight:700;font-size:31px;line-height:40px;color:var(--white);text-transform:uppercase}
.hero-line.left{left:0;top:278px}
.hero-line.right{left:468px;top:278px}
.hero-dots{position:absolute;left:447px;top:376px;display:flex;gap:9px}
.hero-dots span{width:9px;height:9px;border-radius:50%;background:var(--white);opacity:.85}
.hero-dots span:first-child{background:var(--green)}

.btn{display:flex;align-items:center;justify-content:center;background:var(--green);color:var(--white);font-family:"Open Sans",sans-serif;font-weight:700;text-transform:uppercase}
.hero-btn{left:392px;top:420px;width:152px;height:42px;font-size:16px}

.about{left:0;top:812px;width:1200px;height:413px;background:var(--sand)}
.about-title{left:131px;top:87px;font-family:"Open Sans",sans-serif;font-weight:700;font-size:34px;line-height:38px;color:var(--ink-soft);text-transform:uppercase}
.about-text{left:131px;top:188px;width:360px;font-size:11.5px;line-height:19px;color:var(--ink-soft)}
.video{left:598px;top:61px;width:474px;height:289px;background:#000}
.video-frame{position:absolute;left:0;top:32px;width:474px;height:222px;background:linear-gradient(180deg,#121522 0%,#1d1f26 45%,#4b3d22 80%,#151515 100%)}
.video-controls{position:absolute;left:0;bottom:0;width:474px;height:22px;background:#1a1a1a}

.cta{left:0;top:1225px;width:1200px;height:417px;background:radial-gradient(ellipse at 50% 55%,#5a5a5a 0%,#333 45%,#121212 100%)}
.cta-title{left:0;top:156px;width:1200px;text-align:center;font-family:"Open Sans",sans-serif;font-weight:700;font-size:26px;color:var(--white);text-transform:uppercase}
.cta-btn{left:501px;top:239px;width:198px;height:43px;font-size:15px}

.cities-title{left:0;top:1700px;width:1200px;text-align:center;font-family:"Open Sans",sans-serif;font-weight:700;font-size:26px;color:var(--ink-soft);text-transform:uppercase}
.cities-intro{left:0;top:1758px;width:1200px;text-align:center;font-size:12px;line-height:20px;color:var(--ink-soft)}
.cities-intro b{color:var(--green);font-weight:500}

.city{top:1848px;width:288px}
.city-photo{width:288px;height:286px}
.city-name{margin-top:28px;font-family:"Open Sans",sans-serif;font-weight:700;font-size:17px;color:var(--ink);text-transform:uppercase}
.city-sub{margin-top:3px;font-family:"Open Sans",sans-serif;font-weight:700;font-size:11.5px;color:var(--ink);text-transform:uppercase;letter-spacing:.3px}
.city-text{margin-top:10px;width:270px;font-size:11.5px;line-height:19px;color:var(--ink-soft)}
.city-btn{margin-top:14px;width:142px;height:41px;font-size:13px;text-transform:none}

.footer{left:0;top:2405px;width:1200px;height:246px;background:var(--night)}
.footer-base{left:0;top:2651px;width:1200px;height:56px;background:var(--night-deep)}
.footer-name{left:778px;top:2456px;font-size:42px;line-height:50px;font-weight:300;color:var(--white)}
.footer-address{left:781px;top:2528px;font-size:17px;line-height:28px;color:var(--white);font-style:normal}
</style>
</head>
<body>
<div class="page">

  <div class="abs topbar"></div>
  <div class="abs topbar-search"></div>
  <div class="abs social"><span></span><span></span><span></span><span></span></div>
  <svg class="abs search-icon" width="22" height="22" viewBox="0 0 22 22" aria-label="Search">
    <circle cx="11" cy="11" r="10" fill="#fff"/>
    <circle cx="10" cy="10" r="4" fill="none" stroke="#2b2b2b" stroke-width="2"/>
    <line x1="13" y1="13" x2="16" y2="16" stroke="#2b2b2b" stroke-width="2"/>
  </svg>

  <div class="abs brand"><span class="brand-square"></span><span class="brand-name">Quiet Horizon</span></div>

  <nav class="abs nav">
    <span>Home</span><span class="active">Quiet Horizon</span><span>Commercial</span><span>Residential</span><span>Field Services Division</span><span>Education Center</span><span>Our Company</span>
  </nav>

  <section class="abs hero">
    <div class="hero-photo left" role="img" aria-label="Night city skyline with office floors lit up"></div>
    <div class="hero-photo right" role="img" aria-label="Night skyline with dark office towers"></div>
    <p class="hero-line left">Is your lighting<br>wasted for hours<br>every night?</p>
    <p class="hero-line right">We helped create<br>a Quiet Horizon<br>here!</p>
    <div class="hero-dots"><span></span><span></span><span></span></div>
    <a class="abs btn hero-btn">Learn more</a>
  </section>

  <section class="abs about">
    <h2 class="abs about-title">What is<br>a Quiet Horizon?</h2>
    <p class="abs about-text">Watch video from ClipHub and one step closer to us.<br>Donec nec justo eget felis facilisis fermentum, aliquam porttitor mauris sit amet orci pelentesque felis facilisis fermentum. Justo eget felis facilisis fermentum, aliquam porttitor mauris sit amet orci pelentesque felis.</p>
    <div class="abs video">
      <div class="video-frame" role="img" aria-label="Video still of a city skyline at night"></div>
      <svg class="video-controls" width="474" height="22" viewBox="0 0 474 22">
        <polygon points="8,7 14,11 8,15" fill="#ddd"/>
        <rect x="24" y="10" width="330" height="2" fill="#555"/>
        <rect x="24" y="10" width="80" height="2" fill="#8cc63f"/>
        <rect x="405" y="9" width="14" height="4" fill="#aaa"/>
        <circle cx="435" cy="11" r="4" fill="#aaa"/>
        <circle cx="456" cy="11" r="4" fill="none" stroke="#aaa" stroke-width="1.5"/>
      </svg>
    </div>
  </section>

  <section class="abs cta" role="img" aria-label="Blurred city lights at night">
    <h2 class="abs cta-title">I want to be part of the Quiet Horizon in my city!</h2>
    <a class="abs btn cta-btn">Contact us today</a>
  </section>

  <h2 class="abs cities-title">We've launched the Quiet Horizon in these cities</h2>
  <p class="abs cities-intro">Is your building causing the wasted lighting? Look at a photo of your city and see your building. It lit up at night?<br>See images from every 6 months of the same city skyline to see how it is changing. <b>VeloTransit</b> do this!</p>

  <article class="abs city" style="left:129px">
    <div class="city-photo" role="img" aria-label="San Francisco office towers at night" style="background:linear-gradient(180deg,#121212 0%,#2a2218 50%,#5a4020 80%,#1a1410 100%)"></div>
    <h3 class="city-name">San Francisco :</h3>
    <p class="city-sub">Voluptam fugit aut omnis explicabo</p>
    <p class="city-text">Donec nec justo eget felis facilisis fermentum, aliquam porttitor mauris sit amet orci pelentesque felis.</p>
    <a class="btn city-btn">Continue reading</a>
  </article>
  <article class="abs city" style="left:453px">
    <div class="city-photo" role="img" aria-label="Los Angeles skyline at night" style="background:linear-gradient(180deg,#0c0c12 0%,#1a1a26 50%,#5a4628 80%,#241a12 100%)"></div>
    <h3 class="city-name">Los Angeles :</h3>
    <p class="city-sub">Voluptam fugit aut omnis explicabo</p>
    <p class="city-text">Donec nec justo eget felis facilisis fermentum, aliquam porttitor mauris sit amet orci pelentesque felis.</p>
    <a class="btn city-btn">Continue reading</a>
  </article>
  <article class="abs city" style="left:780px">
    <div class="city-photo" role="img" aria-label="New York City towers at night from a rooftop" style="background:linear-gradient(180deg,#0a0a0e 0%,#1c1a22 50%,#3a2c22 80%,#4a3626 100%)"></div>
    <h3 class="city-name">New York City:</h3>
    <p class="city-sub">Voluptam fugit aut omnis explicabo</p>
    <p class="city-text">Donec nec justo eget felis facilisis fermentum, aliquam porttitor mauris sit amet orci pelentesque felis.</p>
    <a class="btn city-btn">Continue reading</a>
  </article>

  <footer>
    <div class="abs footer"></div>
    <div class="abs footer-name">VeloTransit</div>
    <address class="abs footer-address">48 Harbor Lane Suite 210<br>Millbrook, NJ 07001<br>(555) 014-2290</address>
    <div class="abs footer-base"></div>
  </footer>

</div>
</body>
</html>
```